Business Card for Multi-Brand Sportswear Company

We are looking for a business card which represents our company and the multiple brands within it.

The company: Kelt Athletic (LTD)
The brands: Kelt, PawaLuni, VerdantFlex, Grit and Gale

Employees using these cards would be representing Kelt Athletic, rather than any of the individual brands. You will see a current design within the uploaded files, to give some inspiration. The actual text of the brands is not necessary, but the logos should be on there is some format.

Our creative minds on this are stretched, so we are looking for someone to make this their own, and show us what a good business card should look like.

We may like to get these printed with spot gloss, so keep that in mind with your designs.

www.keltathletic.co.uk

Industry/Entity Type

Business

Contact Information for Business Card

Tom Hollingsworth-Pryce
Operations Manager
(+44) 1632 960 418
Tom@keltathletic.co.uk
www.keltathletic.co.uk

Font styles to use
Sans Serif
Other font styles liked:
• Eurostile

Colors
ffffff

Requirements
Nice to have
• Dark (black) background

```html
<!DOCTYPE html>
<html lang="en">
<head>
<meta charset="utf-8">
<title>Kelt Athletic – Business Card</title>
<link rel="stylesheet" href="https://fonts.googleapis.com/css2?family=Saira:wght@400;500;600;700&display=swap">
<style>
  :root {
    --backdrop: #3b3b3b;
    --card-white: #ffffff;
    --card-black: #000000;
    --accent-red: #e3202a;
    --text-grey: #6a6a6a;
    --icon-grey: #9a9a9a;
    --brand-violet: #6b5a7a;
    --white: #ffffff;
  }
  * { box-sizing: border-box; margin: 0; padding: 0; }
  html, body {
    width: 1105px; height: 1200px; overflow: hidden;
    background: var(--backdrop);
    font-family: "Saira", "Helvetica Neue", Arial, sans-serif;
  }
  .card {
    position: absolute; left: 196px; width: 720px; height: 411px;
  }
  .card--front { top: 146px; background: var(--card-white); }
  .card--back { top: 602px; background: var(--card-black); }

  /* Front */
  .wordmark {
    position: absolute; display: flex; align-items: center; gap: 12px;
    font-weight: 600; letter-spacing: 0.5px; line-height: 1;
  }
  .wordmark__square { display: block; background: var(--accent-red); }
  .card--front .wordmark { left: 54px; top: 62px; font-size: 36px; color: var(--card-black); }
  .card--front .wordmark__square { width: 22px; height: 22px; }

  .contact {
    position: absolute; left: 53px; top: 226px;
    color: var(--text-grey); font-size: 19px; line-height: 27px;
  }
  .contact__address { margin-bottom: 6px; }
  .contact__row { display: flex; align-items: center; gap: 10px; }
  .contact__icon { width: 17px; height: 17px; flex: none; }

  .name-tab {
    position: absolute; left: 398px; top: 254px; width: 322px; height: 79px;
    background: var(--card-black);
    clip-path: polygon(28px 0, 100% 0, 100% 100%, 0 100%, 4px 88%);
    border-top-left-radius: 14px;
    text-align: right; padding: 10px 24px 0 0;
  }
  .name-tab__name { color: var(--accent-red); font-size: 25px; font-weight: 600; line-height: 32px; }
  .name-tab__role { color: var(--white); font-size: 19px; line-height: 26px; }

  /* Back */
  .card--back .wordmark {
    left: 50%; top: 138px; transform: translateX(-50%);
    font-size: 66px; color: var(--white); gap: 18px; white-space: nowrap;
  }
  .card--back .wordmark__square { width: 36px; height: 36px; }

  .brand-row { position: absolute; left: 0; top: 344px; width: 100%; height: 34px; }
  .brand {
    position: absolute; top: 0; transform: translateX(-50%);
    font-size: 20px; font-weight: 600; line-height: 34px; white-space: nowrap;
  }
  .brand--pawaluni { left: 84px; color: var(--icon-grey); }
  .brand--verdantflex { left: 257px; color: var(--brand-violet); }
  .brand--grit { left: 430px; color: var(--accent-red); }
  .brand--kelt { left: 602px; color: var(--white); }
</style>
</head>
<body>
  <section class="card card--front">
    <div class="wordmark"><span class="wordmark__square"></span>Kelt Athletic</div>

    <div class="contact">
      <p class="contact__address">Fenwick Yard, Holbrook<br>Ashdale, ZZ9 4QT</p>
      <p class="contact__row">
        <svg class="contact__icon" viewBox="0 0 24 24" aria-hidden="true"><path fill="#e3202a" d="M6.6 10.8a15.1 15.1 0 0 0 6.6 6.6l2.2-2.2c.3-.3.7-.4 1-.2 1.1.4 2.3.6 3.6.6.6 0 1 .4 1 1V20c0 .6-.4 1-1 1A17 17 0 0 1 3 4c0-.6.4-1 1-1h3.5c.6 0 1 .4 1 1 0 1.3.2 2.5.6 3.6.1.3 0 .7-.2 1z"/></svg>
        +44 (0)1632 960418
      </p>
      <p class="contact__row">
        <svg class="contact__icon" viewBox="0 0 24 24" aria-hidden="true"><rect x="2" y="5" width="20" height="14" rx="1" fill="#e3202a"/><path d="M3 6l9 7 9-7" fill="none" stroke="#fff" stroke-width="1.6"/></svg>
        rhys@keltathletic.co.uk
      </p>
      <p class="contact__row">
        <svg class="contact__icon" viewBox="0 0 24 24" aria-hidden="true"><circle cx="12" cy="12" r="10" fill="#e3202a"/><path d="M2 12h20M12 2c3 3 3 17 0 20M12 2c-3 3-3 17 0 20" fill="none" stroke="#fff" stroke-width="1.4"/></svg>
        www.keltathletic.co.uk
      </p>
    </div>

    <div class="name-tab">
      <p class="name-tab__name">Rhys Calloway</p>
      <p class="name-tab__role">Managing Director</p>
    </div>
  </section>

  <section class="card card--back">
    <div class="wordmark"><span class="wordmark__square"></span>Kelt Athletic</div>
    <div class="brand-row">
      <span class="brand brand--pawaluni">PawaLuni</span>
      <span class="brand brand--verdantflex">VerdantFlex</span>
      <span class="brand brand--grit">Grit and Gale</span>
      <span class="brand brand--kelt">Kelt</span>
    </div>
  </section>
</body>
</html>
```